Luxury Brand Real Estate For Sale sign

**Update** I've added some examples from the internet of other signs that have a look similar to what I would like to see. I do not want my personal name in the sign. And the word FOR SALE Does not need to be so large - it can be more subtle.
I want to create a Real Estate for sale sign for my company that will be used for luxury/higher end real estate listings. I’m sharing my business card as well as a logo with new teal color to show what we're moving towards: we’re using Teal, white, black and gold.
Hoping the sign is simple, sophisticated and eye catching.
The sign should be 24" wide by 30" tall including the company name: Harbor Crest Realty Group and our logo, office phone number 727-555-0148 and website www.hcrgexample.com the words "For Sale"
Optional to add this e-mail address info@hcrgexample.com to the sign
Target Market(s)
Luxury home buyers
Industry/Entity Type
Real Estate
Look and feel

```html
<!DOCTYPE html>
<html lang="en">
<head>
<meta charset="utf-8">
<title>Harbor Crest Realty Group – For Sale Sign</title>
<link rel="stylesheet" href="https://fonts.googleapis.com/css2?family=Montserrat:wght@300;400;700&family=Arimo:wght@500&display=swap">
<style>
  :root {
    --backdrop: #e8f5fc;
    --sign-black: #18191b;
    --gold: #f6dd85;
    --ice-white: #eaf6fc;
  }
  html, body {
    margin: 0;
    padding: 0;
    width: 1200px;
    height: 1200px;
    overflow: hidden;
    background: var(--backdrop);
  }
  .canvas {
    display: block;
    width: 1200px;
    height: 1200px;
  }
  .sign-panel { fill: var(--sign-black); }
  .gold-rule { stroke: var(--gold); fill: none; }
  .brand-initials {
    font-family: "Montserrat", sans-serif;
    font-weight: 300;
    font-size: 62px;
    letter-spacing: 2px;
    fill: var(--gold);
  }
  .brand-name {
    font-family: "Montserrat", sans-serif;
    font-weight: 300;
    font-size: 27px;
    letter-spacing: 1.5px;
    fill: var(--gold);
  }
  .brand-subname {
    font-family: "Montserrat", sans-serif;
    font-weight: 300;
    font-size: 18px;
    letter-spacing: 2px;
    fill: var(--gold);
  }
  .headline {
    font-family: "Montserrat", sans-serif;
    font-weight: 700;
    font-size: 74px;
    fill: var(--ice-white);
  }
  .contact-label {
    font-family: "Montserrat", sans-serif;
    font-weight: 300;
    font-size: 34px;
    fill: var(--ice-white);
  }
  .contact-phone {
    font-family: "Montserrat", sans-serif;
    font-weight: 300;
    font-size: 43px;
    fill: var(--gold);
  }
  .contact-web {
    font-family: "Montserrat", sans-serif;
    font-weight: 300;
    font-size: 32px;
    fill: var(--ice-white);
  }
  .contact-mail {
    font-family: "Arimo", sans-serif;
    font-weight: 500;
    font-size: 28px;
    fill: var(--ice-white);
  }
</style>
</head>
<body>
<svg class="canvas" viewBox="0 0 1200 1200" xmlns="http://www.w3.org/2000/svg">
  <rect class="sign-panel" x="246" y="212" width="708" height="776"/>

  <g class="brand">
    <text class="brand-initials" x="430" y="419" text-anchor="middle">HCRG</text>
    <line class="gold-rule" x1="557" y1="338" x2="557" y2="454" stroke-width="3"/>
    <text class="brand-name" x="587" y="395">HARBOR CREST</text>
    <text class="brand-subname" x="587" y="417">REALTY GROUP</text>
  </g>

  <line class="gold-rule" x1="298" y1="470" x2="902" y2="470" stroke-width="4"/>

  <text class="headline" x="600" y="632" text-anchor="middle">FOR SALE</text>

  <g class="contact">
    <text class="contact-label" x="320" y="773">phone number</text>
    <text class="contact-phone" x="583" y="773">727-555-0148</text>
    <text class="contact-web" x="600" y="821" text-anchor="middle">website www.hcrgexample.com</text>
    <text class="contact-mail" x="600" y="855" text-anchor="middle">e-mail info@hcrgexample.com</text>
  </g>
</svg>
</body>
</html>
```